New CD - "Tunes About Marla" (Jazz piano standards)

We need a CD design for album of jazz piano standards. The music is elegant, fun, and artistic. Appeals to all lovers of Halvorsen, Brenton, Dubrow, etc. Includes Red Harbor, Can't Stop Dancin', Harbor Serenade, She Keeps A Secret In Her Pocket, Rain Falls On Quiet Streets, Lazy Tuesday, (Tonight) Across The Meadow, Hours by Candle and Lace, When Rivers Bend, Only If You Call, Your Quiet Spark, She Always Left The Door, Remarkable Dawn, Prelude Op. 41, No. 7 "Lamplight"/T. Varga.

Target Market(s)

Anyone who likes piano music.

```html
<!DOCTYPE html>
<html lang="en">
<head>
<meta charset="utf-8">
<title>Tunes About Marla – Back Inlay</title>
<link rel="stylesheet" href="https://fonts.googleapis.com/css2?family=Bree+Serif&family=Exo+2:wght@300&display=swap">
<style>
  :root {
    --page: #ffffff;
    --maroon-deep: #3a0a0c;
    --maroon: #5c1414;
    --rust: #a8462a;
    --amber: #e8912a;
    --gold: #f6b443;
    --title-ink: #fbf1df;
    --credit-ink: rgba(240, 214, 186, 0.72);
    --legal-ink: rgba(214, 160, 128, 0.85);
  }
  * { margin: 0; padding: 0; box-sizing: border-box; }
  html, body {
    width: 1200px; height: 1000px; overflow: hidden;
    background: var(--page);
  }
  .back-inlay {
    position: absolute;
    left: 180px; top: 135px;
    width: 816px; height: 707px;
    overflow: hidden;
  }
  .backdrop-photo {
    position: absolute; inset: 0;
    background: linear-gradient(172deg,
      var(--rust) 0%,
      var(--maroon) 14%,
      var(--maroon-deep) 38%,
      var(--maroon) 55%,
      var(--amber) 72%,
      var(--maroon) 86%,
      var(--gold) 100%);
  }
  .track-list {
    position: absolute;
    top: 58px; left: 0; width: 100%;
    list-style: none;
  }
  .track {
    display: flex;
    height: 21.8px;
    align-items: baseline;
  }
  .track-title {
    width: 597px;
    text-align: right;
    font-family: "Bree Serif", serif;
    font-size: 18px;
    color: var(--title-ink);
    white-space: nowrap;
    letter-spacing: 0.2px;
  }
  .track-credit {
    margin-left: 13px;
    font-family: "Exo 2", sans-serif;
    font-weight: 300;
    font-size: 11px;
    color: var(--credit-ink);
    white-space: nowrap;
  }
  .legal {
    position: absolute;
    left: 300px; top: 643px; width: 280px;
    text-align: center;
    font-family: "Exo 2", sans-serif;
    font-weight: 300;
    font-size: 14px;
    line-height: 18px;
    color: var(--legal-ink);
  }
</style>
</head>
<body>
  <section class="back-inlay">
    <div class="backdrop-photo" role="img" aria-label="Photograph of warm sunlight falling through window blinds in bands of amber and deep maroon"></div>

    <ol class="track-list">
      <li class="track"><span class="track-title">1. She Keeps A Secret In Her Pocket</span><span class="track-credit">/H. Pellam (2:22)</span></li>
      <li class="track"><span class="track-title">2. Rain Falls On Quiet Streets</span><span class="track-credit">/J. Korvel &amp; O. Marsh (3:25)</span></li>
      <li class="track"><span class="track-title">3. Red Harbor</span><span class="track-credit">/R. Brenton (3:31)</span></li>
      <li class="track"><span class="track-title">4. Lazy Tuesday</span><span class="track-credit">/H. Pellam (2:08)</span></li>
      <li class="track"><span class="track-title">5. Across The Meadow</span><span class="track-credit">/H. Pellam &amp; E.Y. Halden (4:12)</span></li>
      <li class="track"><span class="track-title">6. Hours by Candle and Lace</span><span class="track-credit">/H. Dubrow &amp; J. Wexley (2:54)</span></li>
      <li class="track"><span class="track-title">7. When Rivers Bend</span><span class="track-credit">/H. Stroud (1:51)</span></li>
      <li class="track"><span class="track-title">8. Can't Stop Dancin'</span><span class="track-credit">/F. Brisk (2:15)</span></li>
      <li class="track"><span class="track-title">9. Only If You Call</span><span class="track-credit">/G. Halvorsen (4:17)</span></li>
      <li class="track"><span class="track-title">10. Harbor Serenade</span><span class="track-credit">/K. Tollan &amp; J. Mirek (2:21)</span></li>
      <li class="track"><span class="track-title">11. Your Quiet Spark</span><span class="track-credit">/V. Oakes (3:34)</span></li>
      <li class="track"><span class="track-title">12. She Always Left The Door</span><span class="track-credit">/R. Brenton (2:49)</span></li>
      <li class="track"><span class="track-title">13. Remarkable Dawn</span><span class="track-credit">/G. Halvorsen (2:13)</span></li>
      <li class="track"><span class="track-title">14. Prelude Op. 41, No. 7 "Lamplight"</span><span class="track-credit">/T. Varga (5:46)</span></li>
    </ol>

    <p class="legal">Copyright © 2012 Daniel Corwin<br>All Rights Reserved</p>
  </section>
</body>
</html>
```